Web Design Project - Management Consulting Firm Firm

We need a design to upgrade our website. The design should reflect the core values , branding of the firm & must be benchmarked with the best management consulting firms in the world.

It should have right choice of images , have evoke words / captions that will attract traffic & must be the best design for a contemporary management consulting firm

current website - www.corvalpeaks.biz
Updates

Hello Designers

we are keen to take our website to next level. It should be benchmarked with best management consulting firm's website on look and feel..

i have uploaded the corporate profile ,  mkt strategy..

email me for any clarifications..

Good Luck

Tev

Project Deadline Extended
Reason: We want the best Design!! and we want to extend the deadline by 3 more days.. 10 Days to go..

Any takers??

Target Market(s)

CFO / CIO / CEO / Business owners & Decision makers

Industry/Entity Type

Management Consulting

Requirements
Must have
• Lively ; but not flashy or flamboyant.

It should reflect the brand values / CPC positioning that I will be sharing .

Benchmark and compare with the best consulting firm websites

Nice to have
• Images..but nothing flashy..

benchmark with leading consulting firms websites..
1.veltrosyn
2.Marquell
3. Harwick Advisory Group
4. Pember & Lusk
5. Dravelin
6. Tusk Consulting
Should not have
• Too loud.

```html
<!DOCTYPE html>
<html lang="en">
<head>
<meta charset="utf-8">
<title>CPC — Transformational Consulting</title>
<link rel="stylesheet" href="https://fonts.googleapis.com/css2?family=Arimo:wght@400;700&display=swap">
<style>
:root{
  --accent-red:#cc0000;
  --text-dark:#2a2a2a;
  --text-mid:#555;
  --text-soft:#8a8a8a;
  --line:#e3e3e3;
  --header-top:#ffffff;
  --header-bottom:#eeeeee;
  --footer-bg:#f4f4f4;
  --sky-top:#3f86c9;
  --sky-mid:#8fbde3;
}
*{box-sizing:border-box;margin:0;padding:0}
html,body{width:1200px;height:985px;overflow:hidden}
body{font-family:"Arimo",Arial,sans-serif;background:#fff;color:var(--text-dark);position:relative}
.site-header{position:absolute;left:0;top:0;width:1200px;height:99px;background:linear-gradient(var(--header-top),var(--header-bottom))}
.brand{position:absolute;left:141px;top:32px;font-size:28px;font-weight:700;color:var(--text-dark);letter-spacing:0;line-height:1}
.search{position:absolute;left:889px;top:21px;display:flex}
.search-field{width:145px;height:22px;border:1px solid #ccc;background:#fff}
.search-btn{width:26px;height:22px;background:var(--accent-red);display:flex;align-items:center;justify-content:center}
.main-nav{position:absolute;right:141px;top:63px;font-size:12.5px;color:var(--text-mid);display:flex}
.main-nav a{color:inherit;text-decoration:none}
.main-nav .sep{margin:0 8px;color:#777}
.hero{position:absolute;left:0;top:99px;width:1200px;height:576px;overflow:hidden;
  background:
    linear-gradient(90deg,rgba(29,42,54,.85) 0%,rgba(29,42,54,.2) 22%,rgba(0,0,0,0) 40%,rgba(0,0,0,0) 70%,rgba(40,70,100,.55) 100%),
    radial-gradient(ellipse at 60% 35%,#eef4fa 0%,var(--sky-mid) 25%,var(--sky-top) 60%,#2b5f94 100%)}
.hero-title{position:absolute;left:141px;top:369px;color:#fff;font-weight:700;text-transform:uppercase;line-height:57px;text-shadow:0 2px 4px rgba(0,0,0,.45)}
.hero-title .small{font-size:38px}
.hero-title .big{font-size:56px}
.columns{position:absolute;left:0;top:712px;width:1200px;height:216px}
.col{position:absolute;top:10px}
.col h2{font-size:17.5px;font-weight:400;color:var(--text-dark);line-height:21px;text-transform:uppercase}
.col-about{left:141px;width:262px}
.col-about p{font-size:12px;line-height:15px;color:var(--text-soft);text-align:justify;margin-top:15px}
.col-about p+p{margin-top:15px}
.col-consult{left:469px;width:260px}
.col-serve{left:797px;width:260px}
.divider{position:absolute;top:0;width:1px;height:216px;background:linear-gradient(rgba(0,0,0,0),var(--line) 30%,var(--line) 70%,rgba(0,0,0,0))}
.link-list{list-style:none;margin-top:10px}
.link-list li{display:flex;align-items:center;gap:8px;font-size:13.5px;color:var(--text-soft);height:28px}
.col-serve .link-list{margin-top:12px}
.col-serve .link-list li{height:23.5px}
.bullet{width:14px;height:14px;flex:none}
.site-footer{position:absolute;left:0;top:937px;width:1200px;height:48px;background:var(--footer-bg);border-top:1px solid #e6e6e6;font-size:11.5px;color:var(--text-soft)}
.copyright{position:absolute;left:141px;top:17px}
.footer-links{position:absolute;right:141px;top:17px}
</style>
</head>
<body>
<header class="site-header">
  <div class="brand">CPC</div>
  <div class="search">
    <div class="search-field"></div>
    <div class="search-btn">
      <svg width="16" height="16" viewBox="0 0 16 16"><circle cx="6.5" cy="6.5" r="4.5" fill="none" stroke="#fff" stroke-width="2"/><line x1="10" y1="10" x2="14.5" y2="14.5" stroke="#fff" stroke-width="2.5" stroke-linecap="round"/></svg>
    </div>
  </div>
  <nav class="main-nav">
    <a href="#">Home</a><span class="sep">|</span>
    <a href="#">Who We Are</a><span class="sep">|</span>
    <a href="#">Transformational Consulting</a><span class="sep">|</span>
    <a href="#">Who We Service</a><span class="sep">|</span>
    <a href="#">Clientele</a><span class="sep">|</span>
    <a href="#">Case Studies</a><span class="sep">|</span>
    <a href="#">Insights</a>
  </nav>
</header>

<section class="hero" role="img" aria-label="Upward view of glass skyscrapers against a blue sky with white clouds">
  <h1 class="hero-title"><span class="small">We help in </span><span class="big">Transforming</span><br><span class="small">Your </span><span class="big">Business...</span></h1>
</section>

<section class="columns">
  <div class="col col-about">
    <h2>Who We Are</h2>
    <p>Lorem ipsum dolor sit amet, consectetur adipiscing elit. Sed sit amet sem nisl. Morbi sagittis dolor ut magna lobortis vel pellentesque sem molestie.</p>
    <p>Pellentesque metus massa, adipiscing quis eleifend vitae, venenatis vel libero. Vivamus non ante tellus. Sed porta elit ut justo placerat non rhoncus mauris luctus.</p>
  </div>
  <div class="divider" style="left:434px"></div>
  <div class="col col-consult">
    <h2>Transformational<br>Consulting</h2>
    <ul class="link-list">
      <li><svg class="bullet" viewBox="0 0 14 14"><circle cx="7" cy="7" r="7" fill="#c8c8c8"/><path d="M5.5 4 8.5 7 5.5 10" fill="none" stroke="#fff" stroke-width="1.6"/></svg>Business Transformation Services</li>
      <li><svg class="bullet" viewBox="0 0 14 14"><circle cx="7" cy="7" r="7" fill="#c8c8c8"/><path d="M5.5 4 8.5 7 5.5 10" fill="none" stroke="#fff" stroke-width="1.6"/></svg>Process Transformation Services</li>
      <li><svg class="bullet" viewBox="0 0 14 14"><circle cx="7" cy="7" r="7" fill="#c8c8c8"/><path d="M5.5 4 8.5 7 5.5 10" fill="none" stroke="#fff" stroke-width="1.6"/></svg>Technology&nbsp; Transformation Services</li>
    </ul>
  </div>
  <div class="divider" style="left:753px"></div>
  <div class="col col-serve">
    <h2>Who We Service</h2>
    <ul class="link-list">
      <li><svg class="bullet" viewBox="0 0 14 14"><circle cx="7" cy="7" r="7" fill="#c8c8c8"/><path d="M5.5 4 8.5 7 5.5 10" fill="none" stroke="#fff" stroke-width="1.6"/></svg>Government / Public Sector</li>
      <li><svg class="bullet" viewBox="0 0 14 14"><circle cx="7" cy="7" r="7" fill="#c8c8c8"/><path d="M5.5 4 8.5 7 5.5 10" fill="none" stroke="#fff" stroke-width="1.6"/></svg>Large Group Companies</li>
      <li><svg class="bullet" viewBox="0 0 14 14"><circle cx="7" cy="7" r="7" fill="#c8c8c8"/><path d="M5.5 4 8.5 7 5.5 10" fill="none" stroke="#fff" stroke-width="1.6"/></svg>SME</li>
      <li><svg class="bullet" viewBox="0 0 14 14"><circle cx="7" cy="7" r="7" fill="#c8c8c8"/><path d="M5.5 4 8.5 7 5.5 10" fill="none" stroke="#fff" stroke-width="1.6"/></svg>Multi Nationals</li>
      <li><svg class="bullet" viewBox="0 0 14 14"><circle cx="7" cy="7" r="7" fill="#c8c8c8"/><path d="M5.5 4 8.5 7 5.5 10" fill="none" stroke="#fff" stroke-width="1.6"/></svg>Emirati Entrepreneur Support</li>
      <li><svg class="bullet" viewBox="0 0 14 14"><circle cx="7" cy="7" r="7" fill="#c8c8c8"/><path d="M5.5 4 8.5 7 5.5 10" fill="none" stroke="#fff" stroke-width="1.6"/></svg>Industry Footprint</li>
    </ul>
  </div>
</section>

<footer class="site-footer">
  <div class="copyright">Copyright © 2011 CPC, All Rights Reserved</div>
  <div class="footer-links">Contact us | Site Map | Legal Disclaimer</div>
</footer>
</body>
</html>
```